Natural Supplement Product : Label Revamp

We want to do product label makeover. Please check out our website :www.fernquillworks.com to get a sense of our company.
Points:
1. We want to keep the color scheme the same
2.The beige/yellowish background on the label is to be removed and changed to be white. But please use beige/yellowish color in another way, just not in the background.
3. We want the design to be clean, not overly crowded/designed, and eye catching.
4.If the company logo needs to altered to be consistent with the label design, you may do so.
5. We prefer to keep the curved/wavy green design, so if you could incorporate that in anyway, that would be great.
We want this to be done in Illustrator and please revamp the Magnesium Bisglycinate as the product label that you choose. And please do not make the label revamp to specific to Magnesium Bisglycinate. We want this label to be specific enough, but also function as a base template label that can be replicated for other products. So if it is very particular to Magnesium Bisglycinate, then it can't be replicable across the board.
We can provide you with the illustrator file as well , so please ask for that.
Target Market(s)
Consumers (health food stores, natural supplement stores)
Look and feel

```html
<!DOCTYPE html>
<html lang="en">
<head>
<meta charset="utf-8">
<title>Fernquill Works – Magnesium Bisglycinate Label</title>
<link rel="stylesheet" href="https://fonts.googleapis.com/css2?family=Playfair+Display:wght@700&family=Roboto+Condensed:wght@300;400;700&display=swap">
<style>
  :root {
    --backdrop: #c8c8c8;
    --label-white: #ffffff;
    --forest: #1c4a30;
    --forest-deep: #143a25;
    --cream: #efe9c4;
    --leaf-light: #c9dc8a;
    --leaf-mid: #9cc24a;
    --leaf-dark: #5f9a2c;
    --lime-line: #d8e66a;
    --berry-red: #d43a33;
    --gold: #c9b46a;
  }
  html, body {
    margin: 0;
    padding: 0;
    width: 1200px;
    height: 812px;
    overflow: hidden;
    background: var(--backdrop);
  }
  .canvas {
    position: relative;
    width: 1200px;
    height: 812px;
  }
  .label {
    position: absolute;
    left: 310px;
    top: 31px;
    width: 580px;
    height: 750px;
    display: block;
  }
  .brand-name {
    font-family: "Roboto Condensed", sans-serif;
    font-weight: 700;
    font-size: 34px;
    letter-spacing: 2px;
    fill: var(--forest);
  }
  .product-name {
    font-family: "Playfair Display", serif;
    font-weight: 700;
    font-size: 112px;
    fill: var(--berry-red);
  }
  .product-form {
    font-family: "Roboto Condensed", sans-serif;
    font-weight: 400;
    font-size: 38px;
    fill: var(--forest);
  }
  .product-form .dose { font-weight: 700; }
  .claim-en {
    font-family: "Roboto Condensed", sans-serif;
    font-weight: 700;
    font-size: 40px;
    fill: var(--forest);
  }
  .claim-fr {
    font-family: "Roboto Condensed", sans-serif;
    font-weight: 300;
    font-size: 35px;
    fill: var(--forest);
  }
  .count {
    font-family: "Roboto Condensed", sans-serif;
    font-weight: 700;
    font-size: 33px;
    fill: var(--berry-red);
  }
</style>
</head>
<body>
<main class="canvas">
  <svg class="label" viewBox="0 0 580 750" xmlns="http://www.w3.org/2000/svg" aria-label="Magnesium Bisglycinate supplement label">
    <defs>
      <linearGradient id="cream-fade" x1="0" y1="0" x2="0" y2="1">
        <stop offset="0" stop-color="#efe9c4"/>
        <stop offset="1" stop-color="#ffffff"/>
      </linearGradient>
      <linearGradient id="leaf-field" x1="0" y1="0" x2="1" y2="1">
        <stop offset="0" stop-color="#d5e49c"/>
        <stop offset="0.5" stop-color="#b4d064"/>
        <stop offset="1" stop-color="#8fbb3c"/>
      </linearGradient>
      <linearGradient id="leaf-wave" x1="0" y1="0" x2="1" y2="0">
        <stop offset="0" stop-color="#8ab63a" stop-opacity="0.2"/>
        <stop offset="0.6" stop-color="#6ea432"/>
        <stop offset="1" stop-color="#4f8a28"/>
      </linearGradient>
      <clipPath id="label-clip"><rect width="580" height="750"/></clipPath>
    </defs>

    <g clip-path="url(#label-clip)">
      <rect class="label-ground" width="580" height="750" fill="var(--label-white)"/>

      <!-- top band -->
      <rect class="top-band" x="0" y="0" width="580" height="17" fill="var(--forest)"/>
      <rect class="top-cream" x="0" y="17" width="580" height="20" fill="url(#cream-fade)"/>

      <!-- green wave field -->
      <path class="wave-field" d="M0 300 C120 290 230 330 330 380 C420 420 500 420 580 405 L580 610 L0 610 Z" fill="url(#leaf-field)"/>
      <path class="wave-band" d="M0 330 C140 320 260 380 360 420 C450 455 520 440 580 420 L580 470 C510 480 440 480 350 445 C250 405 140 355 0 370 Z" fill="url(#leaf-wave)" opacity="0.85"/>
      <path class="wave-highlight" d="M0 312 C130 300 240 345 340 392 C430 432 510 430 580 412" fill="none" stroke="#ffffff" stroke-opacity="0.5" stroke-width="3"/>

      <!-- bottom band -->
      <rect class="bottom-lime" x="0" y="596" width="580" height="10" fill="var(--lime-line)"/>
      <rect class="bottom-band" x="0" y="606" width="580" height="144" fill="var(--forest)"/>
      <rect class="bottom-cream" x="0" y="606" width="580" height="3" fill="var(--cream)" opacity="0.6"/>
    </g>

    <!-- brand -->
    <g class="brand">
      <circle cx="190" cy="100" r="11" fill="var(--leaf-mid)"/>
      <text class="brand-name" x="212" y="112">FERNQUILL WORKS</text>
    </g>

    <!-- product -->
    <text class="product-name" x="290" y="285" text-anchor="middle" textLength="540" lengthAdjust="spacingAndGlyphs">Magnesium</text>
    <text class="product-form" x="562" y="334" text-anchor="end">Bisglycinate <tspan class="dose">200 mg</tspan></text>

    <!-- claims -->
    <text class="claim-en" x="238" y="506">High Bioavailability</text>
    <text class="claim-fr" x="238" y="555">Haute Biodisponibilité</text>

    <!-- count -->
    <text class="count" x="238" y="672">90 Vegetable Capsules</text>

    <!-- quality seal -->
    <g class="quality-seal" role="img" aria-label="Quality guarantee seal">
      <circle cx="93" cy="578" r="84" fill="#f4f1e4" stroke="var(--gold)" stroke-width="4"/>
      <circle cx="93" cy="578" r="66" fill="none" stroke="var(--forest)" stroke-width="3"/>
      <circle cx="93" cy="578" r="42" fill="var(--leaf-light)"/>
    </g>
  </svg>
</main>
</body>
</html>
```